Card for invoking rights with police

Our criminal defense law firm is seeking proposals for a design for our card intended for clients to carry with them in their car. Upon being pulled over, they would hand this card to the officer.
Text for the back of the card:
"For Law Enforcement:"
"I will comply with lawful orders but respectfully decline any test or other requests without my attorney. I wish to remain silent, do not consent to searches, and request to speak with my attorney now.
The back of the card should prominently feature the text and the firm logo should be secondary.
Front
Must prominently feature contact info: 503-555-0182. Do not include attorney name, email, phone from the example file. This is intended to be generic for the firm and not tied to an individual lawyer.
Included for design reference: current business card, firm logo.
We intend to use trenvo.com to produce the cards.
Updates
The back of the card should prominently display the text regarding invocation of rights. Please title it "For Law Enforcement".
Target Market(s)
People who have been stopped by police
Contact Information for Business Card
see project description
Look and feel

```html
<!DOCTYPE html>
<html lang="en">
<head>
<meta charset="UTF-8">
<title>For Law Enforcement Card</title>
<link href="https://fonts.googleapis.com/css2?family=Open+Sans:wght@400;700&display=swap" rel="stylesheet">
<style>
  :root {
    --navy: #0b2f4f;
    --white: #ffffff;
  }
  html, body {
    margin: 0;
    padding: 0;
    overflow: hidden;
    background: var(--navy);
  }
  .card {
    position: relative;
    width: 1200px;
    height: 686px;
    background: var(--navy);
    color: var(--white);
    font-family: "Open Sans", sans-serif;
    overflow: hidden;
  }
  .firm-mark {
    position: absolute;
    top: 64px;
    right: 62px;
    display: flex;
    align-items: center;
    gap: 16px;
  }
  .firm-mark__square {
    width: 44px;
    height: 44px;
    background: var(--white);
  }
  .firm-mark__name {
    font-size: 30px;
    font-weight: 400;
    letter-spacing: 0.12em;
    color: var(--white);
    white-space: nowrap;
  }
  .rights-notice {
    position: absolute;
    top: 206px;
    left: 0;
    width: 100%;
    text-align: center;
  }
  .rights-notice__title {
    margin: 0 0 22px;
    font-size: 49px;
    font-weight: 700;
    line-height: 1.2;
  }
  .rights-notice__body {
    margin: 0;
    font-size: 30.5px;
    font-weight: 400;
    line-height: 45px;
  }
</style>
</head>
<body>
  <main class="card">
    <div class="firm-mark">
      <span class="firm-mark__square"></span>
      <span class="firm-mark__name">HALVERN LAW FIRM</span>
    </div>
    <section class="rights-notice">
      <h1 class="rights-notice__title">For Law Enforcement:</h1>
      <p class="rights-notice__body">
        I will comply with lawful orders but respectfully<br>
        decline any test or other requests without my attorney.<br>
        I wish to remain silent, do not consent to searches,<br>
        and request to speak with my attorney now.
      </p>
    </section>
  </main>
</body>
</html>
```